We would like a new design for our company Christmas Card. The design must have an orange background and have a festive theme.

The size of the card should be DL (210mm x 99mm).

Message on front cover: Merry Christmas
Message inside: Our warmest wishes for a wonderful Christmas and a very Happy New Year
From the team at under quiet rafters and tidal-crest

Please see attached example of the card that we used last year.

Industry/Entity Type

It Company

Colors
f78f20

Requirements
Must have
• Orange as the main colour
• A new design
• Font - Helevetica Neue Light (not condensed)

```html
<!DOCTYPE html>
<html lang="en">
<head>
<meta charset="utf-8">
<title>Christmas Card – Front and Inside</title>
<link rel="stylesheet" href="https://fonts.googleapis.com/css2?family=Great+Vibes&family=Roboto:wght@300&display=swap">
<style>
  :root {
    --orange: #f78f20;
    --orange-light: #f9a64a;
    --orange-soft: #fbc58a;
    --orange-pale: #fde3c6;
    --peach-faint: #fbefe3;
    --white: #ffffff;
    --backdrop-top: #050505;
    --backdrop-bottom: #1d1d1d;
  }
  html, body {
    margin: 0;
    padding: 0;
    overflow: hidden;
  }
  .canvas {
    position: relative;
    width: 1200px;
    height: 694px;
    overflow: hidden;
    background: linear-gradient(160deg, var(--backdrop-top) 0%, #111 55%, var(--backdrop-bottom) 100%);
    font-family: "Roboto", "Helvetica Neue", Arial, sans-serif;
  }
  .card-panel {
    position: absolute;
    top: 91px;
    width: 545px;
    height: 512px;
    background: var(--white);
    overflow: hidden;
  }
  .card-front { left: 62px; }
  .card-inside { left: 621px; }

  /* Front cover */
  .front-band {
    position: absolute;
    left: 0;
    top: 255px;
    width: 100%;
    height: 257px;
    background: var(--orange);
  }
  .snowfall-backdrop {
    position: absolute;
    left: 0;
    top: 0;
    width: 100%;
    height: 255px;
    background:
      radial-gradient(circle at 12% 35%, var(--peach-faint) 0%, rgba(251,239,227,0) 12%),
      radial-gradient(circle at 27% 58%, var(--peach-faint) 0%, rgba(251,239,227,0) 11%),
      radial-gradient(circle at 44% 85%, var(--peach-faint) 0%, rgba(251,239,227,0) 11%),
      radial-gradient(circle at 68% 43%, var(--peach-faint) 0%, rgba(251,239,227,0) 11%),
      radial-gradient(circle at 84% 30%, var(--peach-faint) 0%, rgba(251,239,227,0) 12%),
      radial-gradient(circle at 82% 75%, var(--peach-faint) 0%, rgba(251,239,227,0) 11%),
      radial-gradient(circle at 19% 84%, var(--peach-faint) 0%, rgba(251,239,227,0) 11%);
  }
  .dotted-tree {
    position: absolute;
    left: 213px;
    top: 0;
    width: 118px;
    height: 170px;
    background: linear-gradient(180deg, var(--orange-light) 0%, var(--orange-soft) 60%, var(--orange-pale) 100%);
    clip-path: polygon(0 0, 100% 0, 50% 100%);
  }
  .front-flake {
    position: absolute;
    border-radius: 50%;
    background: radial-gradient(circle, rgba(255,255,255,0.55) 0%, rgba(255,255,255,0.3) 45%, rgba(255,255,255,0.12) 70%, rgba(255,255,255,0) 100%);
  }
  .front-flake--large { left: 326px; top: 282px; width: 196px; height: 196px; }
  .front-flake--upper { left: 470px; top: 248px; width: 84px; height: 84px; }
  .front-flake--lower { left: 480px; top: 442px; width: 76px; height: 76px; }
  .front-greeting {
    position: absolute;
    left: 53px;
    top: 350px;
    margin: 0;
    font-family: "Great Vibes", cursive;
    font-weight: 400;
    font-size: 41px;
    line-height: 1;
    color: var(--white);
    white-space: nowrap;
  }

  /* Inside */
  .inside-flake {
    position: absolute;
    border-radius: 50%;
    background: radial-gradient(circle, rgba(247,143,32,0.55) 0%, rgba(247,143,32,0.35) 45%, rgba(247,143,32,0.15) 70%, rgba(247,143,32,0) 100%);
  }
  .inside-flake--tiny-a { left: 428px; top: 44px; width: 36px; height: 36px; }
  .inside-flake--tiny-b { left: 466px; top: 77px; width: 42px; height: 42px; }
  .inside-flake--small { left: 408px; top: 124px; width: 66px; height: 66px; }
  .inside-flake--edge { left: 468px; top: 183px; width: 140px; height: 140px; }
  .inside-flake--large { left: 325px; top: 285px; width: 194px; height: 194px; }
  .inside-flake--corner { left: 480px; top: 442px; width: 76px; height: 76px; }
  .inside-message {
    position: absolute;
    left: 67px;
    top: 364px;
    margin: 0;
    font-weight: 300;
    font-size: 16.5px;
    line-height: 21.5px;
    color: var(--orange);
  }
  .inside-signoff {
    position: absolute;
    left: 67px;
    top: 441px;
    margin: 0;
    font-weight: 300;
    font-size: 10px;
    color: var(--orange);
    white-space: nowrap;
  }
</style>
</head>
<body>
<main class="canvas">
  <section class="card-panel card-front" aria-label="Card front cover">
    <div class="snowfall-backdrop" role="img" aria-label="Faint pale snowflakes and tiny stars scattered across the white sky"></div>
    <div class="dotted-tree" role="img" aria-label="Inverted Christmas tree formed from orange dots and small snowflakes"></div>
    <div class="front-band"></div>
    <div class="front-flake front-flake--large" role="img" aria-label="Large white swirling snowflake ornament"></div>
    <div class="front-flake front-flake--upper" role="img" aria-label="White swirling snowflake ornament at the edge"></div>
    <div class="front-flake front-flake--lower" role="img" aria-label="White swirling snowflake ornament in the corner"></div>
    <h1 class="front-greeting">Merry Christmas</h1>
  </section>

  <section class="card-panel card-inside" aria-label="Card inside message">
    <div class="inside-flake inside-flake--tiny-a" role="img" aria-label="Small orange snowflake ornament"></div>
    <div class="inside-flake inside-flake--tiny-b" role="img" aria-label="Small orange snowflake ornament"></div>
    <div class="inside-flake inside-flake--small" role="img" aria-label="Orange snowflake ornament"></div>
    <div class="inside-flake inside-flake--edge" role="img" aria-label="Orange swirling snowflake ornament at the edge"></div>
    <div class="inside-flake inside-flake--large" role="img" aria-label="Large orange swirling snowflake ornament"></div>
    <div class="inside-flake inside-flake--corner" role="img" aria-label="Orange snowflake ornament in the corner"></div>
    <p class="inside-message">Our warmest wishes<br>for a wonderful Christmas<br>and a very Happy New Year</p>
    <p class="inside-signoff">From the team at under quiet rafters and tidal-crest</p>
  </section>
</main>
</body>
</html>
```